Quiet Harbor Counseling Business Card design with a visually interesting use of Space

I need business cards that are luxurious and give a peaceful, calm vibe. I also had some letterhead designed, and i like the look of it also, it's attached with the logo design for reference/ ideas but feel free to be creative.

Target Market(s)

High end luxurious client who needs counseling

Industry/Entity Type

Marriage and Family Therapy

Contact Information for Business Card

Corra Mabbitt MS LMFT/ or Tobin Walsh address 4175 Pemberly Suite 620

Font styles to use
Sans Serif

Colors
0054AA
0677BA
7BADD7
CADEEF
E8F1F8
0094D4
00A9DD
6FCCEA
C7EBF8
E9F6FB
A7469A
B969AE
D3A5CF
EDDBEB
F8F0F9
6B429C
8869AF
B7A5CE
E3DAEB
F3F0F8

Requirements
Must have
• Logo and color scheme but be simple modern and luxurious
Nice to have
• I'd like to incorporate some elelmets from the logo and letterhead into a simple modern card

```html
<!DOCTYPE html>
<html lang="en">
<head>
<meta charset="utf-8">
<title>Quiet Harbor Counseling — Business Card</title>
<link rel="stylesheet" href="https://fonts.googleapis.com/css2?family=Poppins:wght@300;400;700&display=swap">
<style>
  :root {
    --stage: #1e1e1e;
    --card-light: #ffffff;
    --card-dark: #161616;
    --ink-dark: #111111;
    --ink-light: #f2f2f2;
    --teal: #2f8896;
    --violet: #8869af;
  }
  * { margin: 0; padding: 0; box-sizing: border-box; }
  html, body {
    width: 1200px; height: 900px; overflow: hidden;
    background: var(--stage);
    font-family: "Poppins", sans-serif;
  }
  .canvas {
    width: 1200px; height: 900px;
    display: flex; flex-direction: column; align-items: center; justify-content: center;
    gap: 36px;
  }
  .card {
    width: 720px; height: 400px; position: relative;
  }
  .card--front { background: var(--card-light); }
  .card--back { background: var(--card-dark); color: var(--ink-light); }

  .brand {
    display: flex; align-items: center; gap: 22px;
    font-weight: 300; letter-spacing: 0.02em; line-height: 1.05;
  }
  .brand__dot { border-radius: 50%; background: var(--violet); flex: none; }
  .brand__name span { display: block; }
  .brand__tag { letter-spacing: 0.22em; padding-left: 40%; }

  .card--front .brand {
    position: absolute; left: 0; right: 0; top: 0; bottom: 0;
    justify-content: center; color: var(--ink-dark);
  }
  .card--front .brand__name { font-size: 58px; }
  .card--front .brand__tag { font-size: 30px; }
  .card--front .brand__dot { width: 70px; height: 70px; }

  .card--back .brand {
    position: absolute; left: 56px; top: 52px; color: var(--ink-light);
  }
  .card--back .brand__name { font-size: 36px; }
  .card--back .brand__tag { font-size: 19px; }
  .card--back .brand__dot { width: 46px; height: 46px; order: 2; }

  .divider {
    position: absolute; left: 48px; right: 48px; top: 258px;
    height: 2px; background: var(--teal);
  }
  .person {
    position: absolute; right: 48px; top: 196px; text-align: right;
  }
  .person__name {
    color: var(--teal); font-weight: 700; font-size: 26px; letter-spacing: 0.02em;
    text-transform: uppercase; line-height: 1.1;
  }
  .person__role { font-size: 15px; letter-spacing: 0.04em; }

  .contacts {
    position: absolute; left: 48px; top: 282px; list-style: none;
    font-size: 16px; line-height: 1.7;
  }
  .contacts li { display: flex; align-items: center; gap: 10px; }
  .contacts svg { width: 16px; height: 16px; fill: var(--teal); flex: none; }

  .address {
    position: absolute; right: 48px; top: 282px; text-align: right;
    font-style: normal; font-size: 16px; line-height: 1.7;
  }
</style>
</head>
<body>
<main class="canvas">
  <section class="card card--front" aria-label="Card front">
    <div class="brand">
      <div class="brand__name">
        <span>Quiet Harbor</span>
        <span class="brand__tag">Counseling</span>
      </div>
      <span class="brand__dot" aria-hidden="true"></span>
    </div>
  </section>

  <section class="card card--back" aria-label="Card back">
    <div class="brand">
      <div class="brand__name">
        <span>Quiet Harbor</span>
        <span class="brand__tag">Counseling</span>
      </div>
      <span class="brand__dot" aria-hidden="true"></span>
    </div>

    <div class="person">
      <p class="person__name">Tobin Walsh</p>
      <p class="person__role">OWNER</p>
    </div>

    <div class="divider"></div>

    <ul class="contacts">
      <li>
        <svg viewBox="0 0 24 24" aria-hidden="true"><path d="M6.6 10.8a15.1 15.1 0 0 0 6.6 6.6l2.2-2.2c.3-.3.7-.4 1-.2 1.1.4 2.3.6 3.6.6.6 0 1 .4 1 1V20c0 .6-.4 1-1 1A17 17 0 0 1 3 4c0-.6.4-1 1-1h3.5c.6 0 1 .4 1 1 0 1.3.2 2.5.6 3.6.1.3 0 .7-.2 1z"/></svg>
        555-204-7719
      </li>
      <li>
        <svg viewBox="0 0 24 24" aria-hidden="true"><path d="M7 2h10a2 2 0 0 1 2 2v16a2 2 0 0 1-2 2H7a2 2 0 0 1-2-2V4a2 2 0 0 1 2-2zm0 3v13h10V5zm5 14.2a1 1 0 1 0 0 1.6 1 1 0 0 0 0-1.6z"/></svg>
        555-318-4062
      </li>
      <li>
        <svg viewBox="0 0 24 24" aria-hidden="true"><path d="M2 5h20v2l-10 6L2 7zm0 4.3 10 6 10-6V19H2z"/></svg>
        hello@quietharborcare.com
      </li>
    </ul>

    <address class="address">
      4175 Pemberly Suite 620<br>
      Brookmere, TX 75990, USA<br>
      www.quietharborcare.com
    </address>
  </section>
</main>
</body>
</html>
```